DMVN Website

Hi we require a website with similar attributes and design to this http://style5.tarnbridgepages.com but obviously with all our information and images etc... also attached are our logos please do the design with the yellow logo not the red.

```html
<!DOCTYPE html>
<html lang="en">
<head>
<meta charset="utf-8">
<title>DMVN – Car Engine Service</title>
<link href="https://fonts.googleapis.com/css2?family=Montserrat:wght@400;500;600;700;800&family=Lato:wght@400;700&display=swap" rel="stylesheet">
<style>
:root{
  --ink:#1c1c1c;
  --text:#777;
  --muted:#9a9a9a;
  --blue:#1e6fd9;
  --dark:#1d1d1f;
  --darker:#141416;
  --light:#f3f3f3;
  --card:#eef0f4;
  --white:#fff;
  --line:#dcdcdc;
}
*{margin:0;padding:0;box-sizing:border-box}
html,body{width:1200px;height:4245px;overflow:hidden}
body{position:relative;background:var(--white);font-family:"Lato",Arial,sans-serif;color:var(--text)}
.abs{position:absolute}
h1,h2,h3,.mont{font-family:"Montserrat",Arial,sans-serif}

/* top bar */
.topbar{left:0;top:0;width:1200px;height:51px;background:var(--dark);color:#ddd;font-size:12px}
.brand{left:240px;top:6px;height:39px;width:185px;display:flex;align-items:center;gap:10px;font-family:"Montserrat",sans-serif;font-weight:800;font-size:22px;color:#f2c230;letter-spacing:2px}
.brand .mark{width:18px;height:18px;background:#f2c230}
.info{top:0;height:51px;display:flex;align-items:center;gap:8px}
.info b{color:#fff}

/* nav */
.nav{left:0;top:51px;width:1200px;height:48px;border-bottom:1px solid #eee;background:#fff}
.nav ul{position:absolute;left:243px;top:0;height:48px;display:flex;align-items:center;gap:24px;list-style:none;font-family:"Montserrat",sans-serif;font-size:12px;font-weight:600;color:var(--ink)}

/* hero */
.hero{left:0;top:99px;width:1200px;height:543px;background:radial-gradient(ellipse at 70% 40%,#5d6268 0%,#33373c 45%,#16181b 100%)}
.hero h1{position:absolute;left:0;width:1200px;text-align:center;color:#fff;font-weight:700;line-height:1;font-size:58px;letter-spacing:1px}
.hero p{position:absolute;left:0;width:1200px;top:272px;text-align:center;color:#e4e4e4;font-size:15px;line-height:23px}
.btn{display:inline-block;background:var(--blue);color:#fff;font-family:"Montserrat",sans-serif;font-weight:700;font-size:10px;text-transform:uppercase;text-align:center}
.hero .btn{position:absolute;left:538px;top:357px;width:113px;height:25px;line-height:25px}
.arrow{top:260px;color:#fff;font-size:20px}

/* best service */
.car-art{left:240px;top:720px;width:360px;height:115px;background:linear-gradient(180deg,#f7f7f7,#ececec)}
.best h2{position:absolute;left:657px;top:692px;font-size:23px;color:var(--ink);font-weight:700}
.para{font-size:12px;line-height:17px;color:var(--muted)}
.btn-outline{border:1px solid var(--blue);color:var(--blue);font-size:10px;text-align:center;font-family:"Montserrat",sans-serif}

/* stats */
.stats{left:0;top:925px;width:1200px;height:414px;background:linear-gradient(90deg,#050505 0%,#111 45%,#2c2f33 75%,#111 100%)}
.worker{left:722px;top:90px;width:254px;height:324px;background:linear-gradient(180deg,#c9a48a 0%,#2d5cc0 35%,#1d3f9a 100%)}
.bar-label{left:243px;color:#fff;font-family:"Montserrat",sans-serif;font-size:11px;font-weight:600;text-transform:uppercase}
.bar{left:243px;width:346px;height:22px;background:#fff}
.bar i{display:block;height:100%;background:var(--blue);color:#fff;font-style:normal;font-size:10px;line-height:22px;padding-left:8px}

/* gallery */
.tile{background:linear-gradient(135deg,#4a4a4a,#262626);display:flex;align-items:center;justify-content:center}

/* solve */
.solve{left:0;top:2009px;width:600px;height:405px;background:var(--light)}
.solve h2{position:absolute;left:51px;top:113px;font-size:23px;color:var(--ink);font-weight:700}
.tyre{left:600px;top:2009px;width:600px;height:405px;background:radial-gradient(circle at 25% 25%,#b3262b 0%,#4a1c20 22%,#1e2126 55%,#3c4047 100%)}
.engine{left:0;top:2414px;width:600px;height:402px;background:linear-gradient(135deg,#2b3a55 0%,#3a3d42 40%,#18191b 100%)}
.counters{left:600px;top:2414px;width:600px;height:402px;background:#f6f6f6}
.counter{top:122px;width:261px;height:155px;border:1px solid #333;background:#fff;text-align:center}
.counter .num{position:absolute;top:70px;left:0;width:100%;font-family:"Montserrat",sans-serif;font-size:24px;color:var(--ink);font-weight:500}
.counter .lbl{position:absolute;bottom:0;left:0;width:100%;height:34px;border-top:1px solid #333;line-height:34px;font-size:12px;color:var(--ink)}

/* pricing */
.plan{top:2878px;width:227px;height:249px;background:var(--card);padding:0 22px}
.plan h3{margin-top:20px;font-size:15px;font-weight:500;color:#555;padding-bottom:10px;border-bottom:1px solid #cfd3da}
.plan .price{margin-top:14px;font-family:"Montserrat",sans-serif;font-size:18px;color:var(--ink);font-weight:600}
.plan .price sup{font-size:10px}
.plan .deal{font-size:10px;color:var(--muted);margin-top:2px}
.plan ul{list-style:none;text-align:right;font-size:11px;line-height:13px;color:var(--muted);margin-top:10px}
.plan .btn{position:absolute;left:22px;bottom:23px;width:183px;height:25px;line-height:25px;border-radius:13px}
.news{left:0;top:3176px;width:1200px;text-align:center;font-size:25px;font-weight:700;color:var(--ink)}

/* contact */
.map{left:0;top:3806px;width:600px;height:377px;background:linear-gradient(160deg,#cfe0ee 0%,#e4ebe0 45%,#d5e4ef 100%)}
.contact{left:600px;top:3806px;width:600px;height:377px;background:linear-gradient(180deg,#1c1d20,#26282c)}
.contact h2{position:absolute;left:45px;top:60px;font-size:25px;color:#fff;font-weight:600}
.field{background:#3a3c40;color:#ddd;font-size:11px;padding:0 10px;display:flex;align-items:center;font-family:"Montserrat",sans-serif}
.contact .btn{position:absolute;left:263px;top:300px;width:71px;height:26px;line-height:26px;font-size:9px;text-transform:none}

/* footer */
.footer{left:0;top:4183px;width:1200px;height:62px;background:var(--darker)}
.socials{left:249px;top:22px;display:flex;gap:12px}
.socials span{width:18px;height:18px;border-radius:50%;border:1px solid #777}
.copy{left:730px;top:24px;font-size:11px;color:#aaa}
</style>
</head>
<body>

<header class="abs topbar">
  <div class="abs brand"><span class="mark"></span>DMVN</div>
  <div class="abs info" style="left:458px">
    <svg width="16" height="16" viewBox="0 0 16 16"><circle cx="8" cy="8" r="6.5" fill="none" stroke="#fff" stroke-width="1.4"/><path d="M8 4v4l3 2" stroke="#fff" stroke-width="1.4" fill="none"/></svg>
    <span>Work Time: Mon - Sat, 8am - 5 PM</span>
  </div>
  <div class="abs info" style="left:665px">
    <svg width="14" height="16" viewBox="0 0 14 16"><path d="M7 15s5-5.5 5-9A5 5 0 0 0 2 6c0 3.5 5 9 5 9z" fill="none" stroke="#fff" stroke-width="1.4"/><circle cx="7" cy="6" r="1.8" fill="#fff"/></svg>
    <span>Harlow Bay, 18 Quarry Ln</span>
  </div>
  <div class="abs info" style="left:832px">
    <svg width="14" height="14" viewBox="0 0 14 14"><path d="M3 1l2.5 3-1.5 1.5a8 8 0 0 0 4.5 4.5L10 8.5l3 2.5-1.5 2C6 13 1 8 1 2.5z" fill="#fff"/></svg>
    <b>Phone: +1 555 014 2290</b>
  </div>
</header>

<nav class="abs nav">
  <ul><li>Home</li><li>Shop</li><li>Blog</li><li>Shortcodes ▾</li><li>About</li><li>404</li><li>Contact</li></ul>
  <svg class="abs" style="left:990px;top:17px" width="16" height="14" viewBox="0 0 16 14"><path d="M0 2h16M0 7h16M0 12h16" stroke="#222" stroke-width="2"/></svg>
  <svg class="abs" style="left:1023px;top:17px" width="14" height="14" viewBox="0 0 14 14"><circle cx="6" cy="6" r="4.5" fill="none" stroke="#222" stroke-width="1.8"/><path d="M9.5 9.5L13 13" stroke="#222" stroke-width="1.8"/></svg>
</nav>

<section class="abs hero" role="img" aria-label="Close-up photo of a car engine bay">
  <span class="abs arrow" style="left:22px">‹</span>
  <span class="abs arrow" style="left:1168px">›</span>
  <h1 style="top:144px">CAR</h1>
  <h1 style="top:208px">ENGINE SERVICE</h1>
  <p>Lorem ipsum dolor sit amet, consectetur adipiscing elit, sed do<br>incididunt ut labore et dolore magna aliqua.</p>
  <span class="btn">Our services</span>
</section>

<section class="best">
  <div class="abs car-art" role="img" aria-label="Line drawing of a sports car side profile"></div>
  <h2>Best service in town</h2>
  <p class="abs para" style="left:657px;top:736px;width:258px">Lorem ipsum dolor sit amet, consectetur adipiscing elit, sed do eiusmod tempor incididunt ut labore et dolore magna aliqua. Ut enim minim veniam, quis nostrud exercitation ullamco.</p>
  <span class="abs btn-outline" style="left:657px;top:835px;width:48px;height:22px;line-height:20px">Details</span>
</section>

<section class="abs stats">
  <div class="abs worker" role="img" aria-label="Photo of a smiling mechanic in blue overalls holding a tablet"></div>
  <span class="abs bar-label" style="top:48px">Repaired cars</span>
  <div class="abs bar" style="top:65px"><i style="width:92%">90%</i></div>
  <span class="abs bar-label" style="top:103px">Satisfied customers</span>
  <div class="abs bar" style="top:120px"><i style="width:75%">75%</i></div>
  <span class="abs bar-label" style="top:158px">Successful tests</span>
  <div class="abs bar" style="top:175px"><i style="width:85%">85%</i></div>
  <span class="abs bar-label" style="top:213px">Painted cars</span>
  <div class="abs bar" style="top:230px"><i style="width:96%">95%</i></div>
  <span class="abs bar-label" style="top:268px">Returning customers</span>
  <div class="abs bar" style="top:285px"><i style="width:92%">90%</i></div>
</section>

<section class="gallery">
  <div class="abs tile" style="left:243px;top:1404px;width:227px;height:167px" role="img" aria-label="Photo of a motorcycle"></div>
  <div class="abs tile" style="left:243px;top:1590px;width:227px;height:167px" role="img" aria-label="Photo of a boat"></div>
  <div class="abs tile" style="left:243px;top:1778px;width:227px;height:169px" role="img" aria-label="Photo of a bicycle wheel">
    <svg width="46" height="28" viewBox="0 0 46 28"><circle cx="9" cy="18" r="8" fill="none" stroke="#fff" stroke-width="2"/><circle cx="37" cy="18" r="8" fill="none" stroke="#fff" stroke-width="2"/><path d="M9 18l10-12h14l4 12M19 6l4 12h-14" fill="none" stroke="#fff" stroke-width="2"/></svg>
  </div>
  <div class="abs tile" style="left:487px;top:1404px;width:470px;height:543px" role="img" aria-label="Photo of a car headlight at dusk">
    <svg width="60" height="26" viewBox="0 0 60 26"><path d="M3 19h6m10 0h22m10 0h6v-6l-10-3-8-7H20l-9 7-8 3z" fill="none" stroke="#fff" stroke-width="2"/><circle cx="14" cy="20" r="4" fill="none" stroke="#fff" stroke-width="2"/><circle cx="46" cy="20" r="4" fill="none" stroke="#fff" stroke-width="2"/></svg>
  </div>
</section>

<section class="abs solve">
  <h2>We can solve any problem</h2>
  <p class="abs para" style="left:51px;top:158px;width:500px">Lorem ipsum dolor sit amet, consectetur adipiscing elit, sed do eiusmod tempor incididunt ut labore et dolore magna aliqua.</p>
  <p class="abs para" style="left:51px;top:200px;width:500px">Ut enim ad minim veniam quis nostrud exercitation ullamco. Lorem ipsum dolor sit amet, consectetur adipiscing elit, sed do eiusmod tempor incididunt ut labore et dolore magna aliqua. Ut enim ad minim veniam quis nostrud.</p>
  <span class="abs btn-outline" style="left:51px;top:266px;width:48px;height:22px;line-height:20px">Details</span>
</section>
<div class="abs tyre" role="img" aria-label="Photo of a car tyre tread with a red digital gauge behind it"></div>

<div class="abs engine" role="img" aria-label="Photo of a mechanic in gloves working on an engine"></div>
<section class="abs counters">
  <div class="abs counter" style="left:25px">
    <svg class="abs" style="left:119px;top:38px" width="22" height="22" viewBox="0 0 22 22"><circle cx="11" cy="11" r="7" fill="none" stroke="#222" stroke-width="2"/><circle cx="11" cy="11" r="2.5" fill="#222"/></svg>
    <div class="num">1042</div><div class="lbl">Mechanical Repairs</div>
  </div>
  <div class="abs counter" style="left:308px">
    <svg class="abs" style="left:119px;top:38px" width="22" height="22" viewBox="0 0 22 22"><rect x="4" y="3" width="14" height="16" fill="none" stroke="#222" stroke-width="2"/><path d="M8 8h6M8 12h6" stroke="#222" stroke-width="2"/></svg>
    <div class="num">572</div><div class="lbl">Bodywork Repairs</div>
  </div>
</section>

<section class="pricing">
  <div class="abs plan" style="left:243px">
    <h3>Starter Package</h3>
    <div class="price"><sup>$</sup>99</div><div class="deal">Start Deal</div>
    <ul><li>Machine installation</li><li>Control &amp; testing</li><li>Maintenance</li><li>Insurance</li></ul>
    <span class="btn">Get started</span>
  </div>
  <div class="abs plan" style="left:487px">
    <h3>PRO Package</h3>
    <div class="price"><sup>$</sup>149</div><div class="deal">Best Deal</div>
    <ul><li>Machine &amp; cable installation</li><li>Control &amp; testing system</li><li>Maintenance</li><li>Insurance</li></ul>
    <span class="btn">Get started</span>
  </div>
  <div class="abs plan" style="left:730px">
    <h3>Business Package</h3>
    <div class="price"><sup>$</sup>199</div><div class="deal">Business Package</div>
    <ul><li>Machine &amp; cable installation</li><li>Control &amp; testing system</li><li>Maintenance &amp; repairs</li><li>Dedicated insurance</li></ul>
    <span class="btn">Get started</span>
  </div>
</section>

<h2 class="abs news">Latest news in mechanics</h2>

<div class="abs map" role="img" aria-label="Map of North America with blue location pins"></div>
<section class="abs contact">
  <h2>Get in touch with us</h2>
  <div class="abs field" style="left:45px;top:125px;width:252px;height:37px">First Name</div>
  <div class="abs field" style="left:311px;top:125px;width:258px;height:37px">Email Address</div>
  <div class="abs field" style="left:45px;top:184px;width:252px;height:35px">Last Name</div>
  <div class="abs field" style="left:311px;top:184px;width:258px;height:35px">Subject</div>
  <div class="abs field" style="left:45px;top:241px;width:524px;height:37px">Message</div>
  <span class="btn">Contact us</span>
</section>

<footer class="abs footer">
  <div class="abs socials"><span></span><span></span><span></span><span></span><span></span><span></span><span></span><span></span><span></span></div>
  <p class="abs copy">Copyright 2024 Northgate Studio. All Rights Reserved.</p>
</footer>

</body>
</html>
```